Velorin Australia Pty Ltd - Stationary design

We need letterheads for hard copy print and e-copy word docs, envelopes - landscape and A3, business cards, With compliment slips and a gloss presentation folder to hold up to 20 A4 pages
Would also like to know what font and size would be recommended to suit our brand.
Logo, Colours, Brand and image can be viewed on www.velorin.com.au

Target Market(s)

Those in pain from 30yrs to 80yrs

Industry/Entity Type

Landscape

Requirements
Must have
• Logo as per trademarked logo on web site
Nice to have
• same colours as our web site logo and design
Should not have
• anything looking cheap or too common
text and font needs to be easy to read but very professional in appearance

```html
<!DOCTYPE html>
<html lang="en">
<head>
<meta charset="utf-8">
<title>Velorin Australia – Letterhead</title>
<link rel="stylesheet" href="https://fonts.googleapis.com/css2?family=PT+Sans:wght@700&display=swap">
<style>
  :root {
    --frame: #939598;
    --paper-top: #f1f1f1;
    --paper-bottom: #ffffff;
    --navy: #2e3d6b;
    --sky: #00aeef;
  }
  * { margin: 0; padding: 0; box-sizing: border-box; }
  html, body { width: 866px; height: 1200px; overflow: hidden; background: var(--frame); }
  .letterhead {
    position: relative;
    width: 866px;
    height: 1200px;
    background: var(--frame);
  }
  .sheet {
    position: absolute;
    left: 26px; top: 26px;
    width: 814px; height: 1148px;
    background: linear-gradient(to bottom, var(--paper-top) 0%, var(--paper-bottom) 70%);
    overflow: hidden;
  }
  .contact-line {
    position: absolute;
    left: 8px; top: 32px;
    font-family: "PT Sans", sans-serif;
    font-weight: 700;
    font-size: 15.5px;
    color: var(--navy);
    letter-spacing: 0.1px;
    white-space: nowrap;
  }
  .rule {
    position: absolute;
    left: 0; top: 78px;
    width: 556px; height: 2px;
    background: var(--sky);
  }
  .brand-name {
    position: absolute;
    left: 566px; top: 22px;
    font-family: "PT Sans", sans-serif;
    font-weight: 700;
    color: var(--navy);
    line-height: 1;
  }
  .brand-name .word-main { display: block; font-size: 44px; letter-spacing: 0.5px; }
  .brand-name .word-sub { display: block; font-size: 22px; margin-top: 4px; padding-left: 62px; }
  .footer-bands {
    position: absolute;
    left: 0; bottom: 0;
    width: 814px; height: 31px;
    display: flex;
  }
  .footer-bands .band-sky { width: 407px; background: var(--sky); }
  .footer-bands .band-navy { flex: 1; background: var(--navy); }
</style>
</head>
<body>
  <div class="letterhead">
    <div class="sheet">
      <p class="contact-line">u4/12 Marlow Street, Ashvale QLD 4217, Australia | 1300 482 615</p>
      <div class="rule"></div>
      <div class="brand-name">
        <span class="word-main">Velorin</span>
        <span class="word-sub">Australia</span>
      </div>
      <div class="footer-bands">
        <div class="band-sky"></div>
        <div class="band-navy"></div>
      </div>
    </div>
  </div>
</body>
</html>
```